Design Tweak needed for a current site

Design on top of an existing quiz funnel

Ideally we would like to tweak what we have already built here (moving elements, styles, adding simple elements etc): http://offers.plumrivetdeals.com/can-you-save-on-car-insurance

The flow:
1) User lands on the quiz page
2) User answers X questions and moves through the flow
3) Calculating user results screen
4) User reaches a success screen, and is subsequently redirected

Keys to the design:
1) We need to emphasize the quiz title as that will drive engagement. In this case, this is a quiz to see if you might be eligible to save money on car insurance.

2) At the end of the quiz we need to make it very, very clear that the user is eligible for savings and that in order to complete the process they are being redirected to another page where they need to fill out a form. It is critical that the design communicates this very clearly... We can count down the time left until redirect and we can use any order of elements to make this point. I think our current design does a very bad job of this.

3) We want to have a "calculating" step so that it seems like the page is working in the background

Goals of the design:
1) Polished, high quality experience throughout
2) User is clearly prepared to be redirected to the conversion funnel/landing page at the end
3) User understands the value of completing the quiz

Target Market(s)

designers

Industry/Entity Type

Moving

Number of Pages Required

1 page

Font styles to use
Sans Serif

Colors

Designer to choose colors to be used in the design.

Requirements
Must have
• This quiz funnel is a template so while the current use case is for auto insurance, we would like a design that also would work in other contexts.
Should not have
• We don't want to materially change the core functionality of the quiz itself... redesigning any of the elements or interactions is encouraged though

```html
<!DOCTYPE html>
<html lang="en">
<head>
<meta charset="utf-8">
<title>PlumRivet Deals – Car Insurance Savings Quiz</title>
<link href="https://fonts.googleapis.com/css2?family=Open+Sans:wght@400;600;700&display=swap" rel="stylesheet">
<style>
  :root {
    --page-bg: #ece9ea;
    --card-bg: #ffffff;
    --ink: #111111;
    --ink-soft: #444444;
    --muted: #8a8a8a;
    --blue: #0a6fe0;
    --green: #3cc068;
    --yellow: #ffd21f;
    --pill-bg: #ededed;
    --border: #a9a9a9;
    --photo-top: #2a2f3a;
    --photo-bottom: #11151d;
  }
  * { box-sizing: border-box; margin: 0; padding: 0; }
  html, body { width: 1200px; height: 630px; overflow: hidden; }
  body {
    background: var(--page-bg);
    font-family: "Open Sans", Arial, sans-serif;
    color: var(--ink);
    position: relative;
  }
  .quiz-card {
    position: absolute; left: 90px; top: 93px;
    width: 1015px; height: 440px;
    background: var(--card-bg);
    border-radius: 5px;
    box-shadow: 0 4px 18px rgba(0,0,0,.14);
    overflow: hidden;
  }
  .brand {
    position: absolute; left: 44px; top: 47px;
    display: flex; align-items: center; gap: 8px;
    font-size: 25px; font-weight: 400; color: var(--ink);
  }
  .brand-dot { width: 22px; height: 22px; border-radius: 50%; background: var(--ink); }
  .quiz-title {
    position: absolute; left: 44px; top: 99px;
    font-size: 20px; font-weight: 700;
  }
  .quiz-subtitle {
    position: absolute; left: 44px; top: 134px;
    font-size: 13.2px; color: var(--ink-soft);
  }
  .progress {
    position: absolute; left: 40px; top: 169px;
    width: 490px; height: 27px;
    background: var(--pill-bg); border-radius: 14px;
    display: flex; align-items: center; padding-left: 7px; gap: 14px;
    list-style: none;
  }
  .step { display: flex; align-items: center; gap: 6px; font-size: 11.2px; color: var(--muted); }
  .step.is-done { color: var(--ink); }
  .step-mark {
    width: 18px; height: 18px; border-radius: 50%;
    border: 1px solid #c9c9c9; background: #f4f4f4;
    display: flex; align-items: center; justify-content: center;
  }
  .step-mark.is-green { background: var(--green); border-color: var(--green); }
  .step-mark.is-blue { background: var(--blue); border-color: var(--blue); }
  .question {
    position: absolute; left: 44px; top: 212px;
    font-size: 17.5px; font-weight: 700; text-transform: uppercase;
  }
  .options { position: absolute; left: 44px; top: 256px; display: flex; gap: 20px; }
  .option {
    position: relative;
    width: 165px; height: 101px;
    border: 1px solid var(--border); border-radius: 3px;
    background: var(--card-bg);
    display: flex; flex-direction: column; align-items: center; justify-content: center; gap: 10px;
    font-size: 9.6px; font-weight: 700; color: var(--ink);
  }
  .option svg { stroke: var(--ink); }
  .option.is-selected {
    background: var(--blue); border-color: var(--blue); color: #fff;
    box-shadow: 0 22px 14px -14px rgba(10,80,180,.35);
  }
  .option.is-selected svg { stroke: #fff; }
  .option-check {
    position: absolute; left: 10px; top: 9px;
    width: 22px; height: 22px; border-radius: 50%;
    background: #fff; display: flex; align-items: center; justify-content: center;
    box-shadow: 0 1px 3px rgba(0,0,0,.25);
  }
  .next-button {
    position: absolute; left: 436px; top: 388px;
    width: 142px; height: 30px;
    background: var(--green); color: #fff; border: 0; border-radius: 2px;
    font-family: inherit; font-size: 9.6px; font-weight: 700; letter-spacing: 1px;
    display: flex; align-items: center; justify-content: space-between; padding: 0 14px 0 18px;
  }
  .call-panel { position: absolute; inset: 0; pointer-events: none; }
  .agent-photo {
    position: absolute; left: 626px; top: 19px;
    width: 280px; height: 421px;
    background: linear-gradient(180deg, var(--photo-top), var(--photo-bottom));
    border-radius: 120px 120px 0 0;
  }
  .call-brand {
    position: absolute; left: 836px; top: 45px;
    display: flex; align-items: center; gap: 6px;
    font-size: 19px; color: #fff;
  }
  .call-brand-dot { width: 18px; height: 18px; border-radius: 50%; background: #fff; }
  .call-note { position: absolute; left: 827px; width: 184px; text-align: center; top: 79px; font-size: 10px; color: #fff; }
  .call-number { position: absolute; left: 827px; width: 184px; text-align: center; top: 95px; font-size: 13px; font-weight: 700; color: var(--yellow); }
</style>
</head>
<body>
<main class="quiz-card">
  <svg class="call-panel" width="1015" height="440" viewBox="0 0 1015 440" aria-hidden="true">
    <polygon points="830,0 1015,0 1015,440 590,440" fill="var(--blue)"/>
  </svg>

  <div class="brand"><span class="brand-dot"></span>PlumRivet Deals</div>
  <h1 class="quiz-title">Quiz: Are You Overpaying For Car Insurance?</h1>
  <p class="quiz-subtitle">Take our five question quiz to see if you might be eligible for car insurance savings</p>

  <ol class="progress">
    <li class="step is-done"><span class="step-mark is-green"><svg width="10" height="8" viewBox="0 0 10 8"><path d="M1 4l3 3 5-6" fill="none" stroke="#fff" stroke-width="1.8"/></svg></span>Question 1</li>
    <li class="step is-done"><span class="step-mark is-blue"><svg width="10" height="8" viewBox="0 0 10 8"><path d="M1 4l3 3 5-6" fill="none" stroke="#fff" stroke-width="1.8"/></svg></span>Question 2</li>
    <li class="step"><span class="step-mark"></span>Question 3</li>
    <li class="step"><span class="step-mark"></span>Question 4</li>
    <li class="step"><span class="step-mark"></span>Question 5</li>
  </ol>

  <h2 class="question">What kind of car do you drive:</h2>

  <div class="options">
    <div class="option is-selected">
      <span class="option-check"><svg width="12" height="10" viewBox="0 0 12 10"><path d="M1 5l3.5 3.5L11 1.5" fill="none" stroke="var(--blue)" stroke-width="2"/></svg></span>
      <svg width="64" height="28" viewBox="0 0 64 28" fill="none" stroke-width="1.3">
        <path d="M3 20v-5l8-3 10-7h20l11 7 7 2v6H3z"/>
        <circle cx="15" cy="21" r="4.5" fill="var(--blue)"/><circle cx="49" cy="21" r="4.5" fill="var(--blue)"/>
        <path d="M22 12h24M33 5v7"/>
      </svg>
      A SEDAN
    </div>
    <div class="option">
      <svg width="64" height="30" viewBox="0 0 64 30" fill="none" stroke-width="1.3">
        <path d="M3 22v-8l6-2 7-9h34l8 9v10H3z"/>
        <circle cx="15" cy="23" r="5" fill="#fff"/><circle cx="49" cy="23" r="5" fill="#fff"/>
        <path d="M18 12h36M34 3v9"/>
      </svg>
      AN SUV
    </div>
    <div class="option">
      <svg width="54" height="42" viewBox="0 0 54 42" fill="none" stroke-width="1.3">
        <rect x="26" y="3" width="22" height="18"/><path d="M32 3v18M4 28v-8h22v8M48 21v7"/>
        <circle cx="12" cy="33" r="6" fill="#fff"/><circle cx="40" cy="32" r="8" fill="#fff"/>
        <circle cx="40" cy="32" r="3"/><circle cx="12" cy="33" r="2"/>
      </svg>
      OTHER
    </div>
  </div>

  <button class="next-button" type="button">NEXT QUESTION
    <svg width="7" height="11" viewBox="0 0 7 11"><path d="M1 1l4.5 4.5L1 10" fill="none" stroke="#fff" stroke-width="1.4"/></svg>
  </button>

  <div class="agent-photo" role="img" aria-label="Smiling insurance agent in a dark suit giving a thumbs up"></div>

  <div class="call-brand"><span class="call-brand-dot"></span>PlumRivet Deals</div>
  <p class="call-note">Get quotes over the phone.</p>
  <p class="call-number">Call Now: (555) 014-7730</p>
</main>
</body>
</html>
```